Power Point Digital Signage Template Needed

The North Halvoran Health Centre and Pharmacy (myhalvoran.example) needs a power point digital signage template that is customizable and pulls pertinent local information like weather, news and generic health tips. Please use design and colors from art work and website. We would need the power point project to be able to be read clearly at a distance of around 10 - 15 feet and provide the viewer with all information about our clinic/pharmacy services while attracting their attention with local news or weather reports and health tips.

Target Market(s)

People in waiting room, healthcare , family doctor patients to drive pharmacy business and healthcare centre awareness

Industry/Entity Type

Healthcare

Font styles to use
Serif
Sans Serif

Colors

Designer to choose colors to be used in the design.

Requirements
Must have
• Links to real time local weather
• Scrolling News
• Scrolling Health tips
• Fully Customizable
• Power Point Format
• Multiple Slides for each feature (example 1 for real time weather, 1 slide for news, 1 slide for cliinic hours etc)
• At least 20 customizable slides on contiual rotation

```html
<!DOCTYPE html>
<html lang="en">
<head>
<meta charset="utf-8">
<title>North Halvoran Digital Signage Template</title>
<link href="https://fonts.googleapis.com/css2?family=Oswald:wght@500&family=Roboto:wght@400;500;700&display=swap" rel="stylesheet">
<style>
  :root {
    --canvas: #ebebeb;
    --blue: #1f98d9;
    --blue-light: #4fb6ea;
    --blue-deep: #0e7fc0;
    --teal-dark: #0c3c4e;
    --teal: #1a7d99;
    --green: #1a8a3e;
    --ink: #3a3a3a;
    --label: #6b6b6b;
    --white: #ffffff;
    --sun: #f6df3a;
    --cloud: #7d9be0;
    --cloud-deep: #4a6bc4;
  }
  * { margin: 0; padding: 0; box-sizing: border-box; }
  html, body { width: 1200px; height: 1027px; overflow: hidden; }
  body { background: var(--canvas); position: relative; font-family: "Roboto", Arial, sans-serif; color: var(--ink); }

  .slide { position: absolute; width: 548px; height: 308px; background: var(--white); overflow: hidden; box-shadow: 0 1px 4px rgba(0,0,0,.25); }
  .slide--cover { left: 30px; top: 42px; background: radial-gradient(ellipse at 30% 30%, #2b9cb8 0%, var(--teal) 40%, var(--teal-dark) 100%); }
  .slide--weather { left: 622px; top: 42px; }
  .slide--news { left: 30px; top: 420px; }
  .slide--hours { left: 622px; top: 420px; }

  .slide-label { position: absolute; width: 548px; text-align: center; font: 700 17px "Roboto", Arial, sans-serif; color: var(--label); letter-spacing: .3px; }

  .cover-title { position: absolute; left: 17px; top: 126px; color: var(--white); font: 500 35px/1 "Oswald", sans-serif; letter-spacing: .3px; }
  .cover-sub { position: absolute; left: 18px; top: 167px; color: var(--white); font: 500 16.5px/1 "Oswald", sans-serif; letter-spacing: .4px; }

  .header-band { position: absolute; left: 0; top: 0; width: 100%; height: 46px; background: linear-gradient(180deg, var(--blue-light), var(--blue)); display: flex; align-items: center; justify-content: center; }
  .header-band h2 { color: var(--white); font: 700 17px "Roboto", Arial, sans-serif; letter-spacing: .2px; }
  .bottom-band { position: absolute; left: 0; bottom: 0; width: 100%; height: 4px; background: var(--blue); }

  .url-rule { position: absolute; left: 181px; top: 286px; width: 187px; height: 8px; display: flex; align-items: center; gap: 4px; }
  .url-rule .line { flex: 1; height: 1px; background: var(--blue); position: relative; }
  .url-rule .line::before { content: ""; position: absolute; top: -2px; width: 5px; height: 5px; border: 1px solid var(--blue); border-radius: 50%; background: var(--white); }
  .url-rule .line--left::before { left: -2px; }
  .url-rule .line--right::before { right: -2px; }
  .url-rule span { font: 500 6px "Roboto", sans-serif; color: var(--blue); letter-spacing: .4px; }
  .slide--cover .url-rule .line { background: var(--white); }
  .slide--cover .url-rule .line::before { border-color: var(--white); background: transparent; }
  .slide--cover .url-rule span { color: var(--white); }

  .page-no { position: absolute; left: 522px; top: 286px; font: 700 6px "Roboto", sans-serif; color: var(--blue); }

  .footer-brand { position: absolute; left: 17px; top: 276px; display: flex; align-items: center; gap: 3px; }
  .footer-brand i { width: 9px; height: 9px; border-radius: 50%; background: var(--green); }
  .footer-brand span { font: 500 7px "Roboto", sans-serif; color: var(--green); }

  .tick-list { position: absolute; list-style: none; }
  .tick-list li { display: flex; align-items: center; gap: 5px; font-size: 6px; color: var(--ink); height: 14px; }
  .tick-list li svg { width: 7px; height: 7px; flex: none; }
  .tick-list li.sub { padding-left: 34px; }
  .tick-list li.sub::before { content: ""; width: 3px; height: 3px; border-radius: 50%; background: var(--blue-deep); }

  .photo { position: absolute; }
  .photo--meter { left: 201px; top: 71px; width: 231px; height: 174px; background: linear-gradient(160deg, #5a8a2e, #3d6b1e 60%, #6a5a3a); }
  .photo--gauge { left: 437px; top: 71px; width: 95px; height: 174px; background: linear-gradient(180deg, #cfd6dc, #e9ecef 50%, #b8bfc4); }
  .photo--beach { left: 201px; top: 71px; width: 231px; height: 174px; background: linear-gradient(180deg, #5fa7e0 0%, #8fc2ea 62%, #4b84a8 75%, #c7a46a 100%); }
  .photo--juice { left: 437px; top: 71px; width: 95px; height: 85px; background: linear-gradient(160deg, #f0a23a, #e87b1c 55%, #8a6a4a); }
  .photo--yoga { left: 437px; top: 162px; width: 95px; height: 82px; background: linear-gradient(180deg, #2d8ed6, #6fb3e6 70%, #b9a88a); }
  .art--weather { position: absolute; left: 394px; top: 68px; width: 128px; height: 184px; border-radius: 8px; background: linear-gradient(160deg, var(--sun) 0%, #c9d46a 22%, var(--cloud) 55%, var(--cloud-deep) 100%); }

  .news-body { position: absolute; left: 46px; top: 91px; width: 322px; }
  .news-body h3 { font: 500 11.5px "Roboto", sans-serif; color: var(--ink); margin-bottom: 6px; }
  .news-body p { font-size: 5.6px; line-height: 9.6px; color: var(--ink); }
  .news-body .tick-list { position: static; margin: 7px 0 6px; }
  .news-body .tick-list li { height: 17px; }

  .brand { position: absolute; left: 310px; top: 840px; display: flex; align-items: center; gap: 26px; }
  .brand i { width: 150px; height: 150px; border-radius: 50%; background: var(--green); }
  .brand-name { color: var(--green); font-family: "Roboto", sans-serif; font-weight: 500; }
  .brand-name b { display: block; font-weight: 500; font-size: 50px; line-height: 1; }
  .brand-name small { display: block; font-size: 15.5px; letter-spacing: 3px; margin-top: 10px; padding-left: 60px; }
</style>
</head>
<body>

<svg width="0" height="0" style="position:absolute" aria-hidden="true">
  <symbol id="tick" viewBox="0 0 10 10">
    <circle cx="5" cy="5" r="4.2" fill="none" stroke="#1f98d9" stroke-width="1"/>
    <path d="M3 5.2 L4.5 6.6 L7 3.8" fill="none" stroke="#1f98d9" stroke-width="1"/>
  </symbol>
</svg>

<section class="slide slide--cover" role="img" aria-label="Rain drops on a window over a blurred street">
  <h1 class="cover-title">NORTH HALVORAN</h1>
  <p class="cover-sub">HEALTH CENTRE &amp; PHARMACY</p>
  <div class="url-rule"><div class="line line--left"></div><span>www.myhalvoran.example</span><div class="line line--right"></div></div>
</section>
<p class="slide-label" style="left:30px;top:368px">COVER PAGE</p>

<section class="slide slide--weather">
  <header class="header-band"><h2>REAL TIME LOCAL WEATHER</h2></header>
  <ul class="tick-list" style="left:40px;top:75px">
    <li><svg><use href="#tick"/></svg>Lorem Ipsum is simply</li>
    <li><svg><use href="#tick"/></svg>Lorem Ipsum is simply</li>
    <li><svg><use href="#tick"/></svg>Lorem Ipsum is simply</li>
    <li><svg><use href="#tick"/></svg>Lorem Ipsum is simply</li>
    <li class="sub">Lorem Ipsum is simply text</li>
    <li class="sub">Lorem Ipsum is simply text</li>
    <li class="sub">Lorem Ipsum is simply text</li>
    <li><svg><use href="#tick"/></svg>Lorem Ipsum is simply</li>
    <li class="sub">Lorem Ipsum is simply text</li>
    <li><svg><use href="#tick"/></svg>Lorem Ipsum is simply</li>
    <li class="sub">Lorem Ipsum is simply text</li>
    <li><svg><use href="#tick"/></svg>Lorem Ipsum is simply</li>
  </ul>
  <div class="photo photo--meter" role="img" aria-label="Digital weather station display standing on grass"></div>
  <div class="photo photo--gauge" role="img" aria-label="Recording rain gauge with chart drum"></div>
  <div class="footer-brand"><i></i><span>North Halvoran</span></div>
  <div class="url-rule"><div class="line line--left"></div><span>www.myhalvoran.example</span><div class="line line--right"></div></div>
  <span class="page-no">01</span>
  <div class="bottom-band"></div>
</section>
<p class="slide-label" style="left:622px;top:368px">PAGE NO - 01</p>

<section class="slide slide--news">
  <header class="header-band"><h2>WEATHER NEWS</h2></header>
  <div class="news-body">
    <h3>WHAT IS LOREM IPSUM</h3>
    <p>Lorem Ipsum is simply dummy text of the printing and typesetting industry. Lorem Ipsum has been the industry's standard dummy text ever since the 1500s, when an unknown printer took a galley of type and scrambled it to make a type specimen book. It has survived not only five centuries, but also the leap into electronic typesetting, remaining essentially unchanged. It was popularised in the 1960s with the release of Letraset sheets containing Lorem.</p>
    <ul class="tick-list">
      <li><svg><use href="#tick"/></svg>Lorem Ipsum is simply dummy text of the printing and typesetting industry. Lorem Ipsum has been the industry.</li>
      <li><svg><use href="#tick"/></svg>Lorem Ipsum is simply dummy text of the printing and typesetting industry. Lorem Ipsum has been the industry.</li>
    </ul>
    <p>Lorem Ipsum is simply dummy text of the printing and typesetting industry. Lorem Ipsum has been the industry's standard dummy text ever since the 1500s, when an unknown printer took a galley of type and scrambled it to make a type specimen book. It has survived not only five centuries, but also the leap into electronic typesetting, remaining essentially unchanged. It was popularised in the 1960s with the release of Letraset sheets containing Lorem Ipsum passages, and more recently with desktop publishing software.</p>
  </div>
  <div class="art--weather" role="img" aria-label="Weather icons: suns, clouds, rain and storm with temperatures 23°, 19°, 21° and 18°"></div>
  <div class="footer-brand"><i></i><span>North Halvoran</span></div>
  <div class="url-rule"><div class="line line--left"></div><span>www.myhalvoran.example</span><div class="line line--right"></div></div>
  <span class="page-no">02</span>
  <div class="bottom-band"></div>
</section>
<p class="slide-label" style="left:30px;top:744px">PAGE NO - 02</p>

<section class="slide slide--hours">
  <header class="header-band"><h2>CLIINIC HOURS</h2></header>
  <ul class="tick-list" style="left:40px;top:73px">
    <li style="height:22px"><svg><use href="#tick"/></svg>Lorem Ipsum is simply dummy text</li>
    <li style="height:22px"><svg><use href="#tick"/></svg>Lorem Ipsum is simply dummy text</li>
    <li style="height:22px"><svg><use href="#tick"/></svg>Lorem Ipsum is simply dummy text</li>
    <li style="height:22px"><svg><use href="#tick"/></svg>Lorem Ipsum is simply dummy text</li>
    <li style="height:22px"><svg><use href="#tick"/></svg>Lorem Ipsum is simply dummy text</li>
    <li style="height:22px"><svg><use href="#tick"/></svg>Lorem Ipsum is simply dummy text</li>
    <li style="height:22px"><svg><use href="#tick"/></svg>Lorem Ipsum is simply dummy text</li>
  </ul>
  <div class="photo photo--beach" role="img" aria-label="Woman jumping joyfully on a beach"></div>
  <div class="photo photo--juice" role="img" aria-label="Glass of orange juice with cut oranges"></div>
  <div class="photo photo--yoga" role="img" aria-label="Person in a yoga pose by the sea"></div>
  <div class="footer-brand"><i></i><span>North Halvoran</span></div>
  <div class="url-rule"><div class="line line--left"></div><span>www.myhalvoran.example</span><div class="line line--right"></div></div>
  <span class="page-no">03</span>
  <div class="bottom-band"></div>
</section>
<p class="slide-label" style="left:622px;top:744px">PAGE NO - 03</p>

<div class="brand">
  <i></i>
  <p class="brand-name"><b>North Halvoran</b><small>Health Centre + Pharmacy</small></p>
</div>

</body>
</html>
```